Tech Company requires UI design for mobile app

We need a mobile app design for a company based in Singapore called "Kalvor Systems". We develop innovative Android/iOS business applications. KalvorLink - a collaboration tool targeted at SMEs that improves reporting and communication between different departments of an organisation. We would like to see designs that use the colour orange, our corporate colour. The final design should communicate clean and technology inclined design.

You are expected to recreate the icons, layout and structure without affecting the workflow.This is a workplace app for employee on mobile. The mobile app aims to empower individual employee to complete the following processes:

1. HR processes - taking attendance, timesheet, employment management to payslip)
2. Inventory management - stock taking, gift redemption and real-time stock management
3. Digital form - application for inspection, safety, procurement or request creation)
4. Job - an app that allows web portal to assign work to individual worker.
Updates

Reason: Received feedback to extens timeline. Cheers!

Target Market(s)

C-Executive, office employee, retail promoter, worker

Industry/Entity Type

Business

Colors

Designer to choose colors to be used in the design.

Requirements
Must have
• - Design must be neat, looks professional and perceived to be user-friendly
• - Use colour theme for each category
• - Must complement with KalvorLink logo them (already attached)
• - Have "apple" feel
• - We like the layout reference 1 & reference 2 photo. However, we prefer a better colour theme (Already Attached)
• - Please download the link for the work required
• https://files.quillbox.example/open?id=7Hq2LmPzXw9RtNc4VbKjYs8DfGaTe3Uo
Nice to have
• More info to follow shortly
Should not have
• - Must not be loud, flashy, dull, bored,
• - Design should not clash with Kalvor Link Logo
• -

```html
<!DOCTYPE html>
<html lang="en">
<head>
<meta charset="utf-8">
<title>KalvorLink – Dashboard</title>
<link href="https://fonts.googleapis.com/css2?family=Roboto:wght@400;500&display=swap" rel="stylesheet">
<style>
:root{
  --stage:#141414;
  --orange-top:#f47a22;
  --orange-bottom:#f04b24;
  --accent:#f26522;
  --ink:#2e2e2e;
  --label:#4a4a4a;
  --panel:#f7f7f7;
  --rule:#e2e2e2;
  --white:#ffffff;
}
*{box-sizing:border-box;margin:0;padding:0}
html,body{width:960px;height:1200px;overflow:hidden;background:var(--stage);font-family:"Roboto",sans-serif}
.screen{position:absolute;left:154px;top:20px;width:560px;height:997px;transform:scale(1.1643);transform-origin:top left;background:var(--white);overflow:hidden}
.header{position:absolute;left:0;top:0;width:560px;height:157px;background:linear-gradient(180deg,var(--orange-top),var(--orange-bottom))}
.status-bar{position:absolute;left:0;top:0;width:100%;height:30px;color:var(--white);font-size:17px;font-weight:500}
.status-bar .time{position:absolute;left:0;right:0;top:5px;text-align:center}
.status-bar .signal{position:absolute;left:10px;top:8px}
.status-bar .battery{position:absolute;right:10px;top:6px;display:flex;align-items:center;gap:6px}
.brand{position:absolute;left:24px;top:44px;display:flex;align-items:center;gap:8px;color:var(--white);font-size:25px;font-weight:400}
.brand .dot{width:14px;height:14px;border-radius:50%;background:var(--white)}
.header-actions{position:absolute;right:16px;top:42px;display:flex;gap:30px}
.employee-name{position:absolute;left:164px;top:115px;color:var(--white);font-size:28px;font-weight:500}
.employee-id{position:absolute;left:163px;top:165px;color:var(--ink);font-size:25px}
.avatar{position:absolute;left:29px;top:103px;width:106px;height:106px;border-radius:50%;border:3px solid var(--white);background:radial-gradient(circle at 50% 40%,#8a6a55,#3a2e2a 70%,#1e1e24)}
.section-title{position:absolute;left:30px;font-size:24px;color:var(--ink)}
.tiles{position:absolute;left:30px;width:530px;display:grid;grid-template-columns:repeat(4,127px);padding-left:-5px}
.tiles.attendance{background:var(--panel)}
.tile{display:flex;flex-direction:column;align-items:center;text-align:center;color:var(--label);font-size:18px;line-height:24px}
.tile svg{width:52px;height:52px;margin-bottom:20px}
.rule{position:absolute;left:30px;right:0;height:1px;background:var(--rule)}
.tab-bar{position:absolute;left:0;top:923px;width:560px;height:74px;background:linear-gradient(180deg,var(--orange-top),var(--orange-bottom));display:grid;grid-template-columns:repeat(4,140px)}
.tab{display:flex;flex-direction:column;align-items:center;padding-top:8px;font-size:14px;color:rgba(255,255,255,.75)}
.tab.active{color:var(--white)}
.tab svg{width:40px;height:40px;margin-bottom:6px}
svg .line{fill:none;stroke:var(--ink);stroke-width:2;stroke-linecap:round;stroke-linejoin:round}
svg .hot{fill:none;stroke:var(--accent);stroke-width:2;stroke-linecap:round;stroke-linejoin:round}
svg .dotfill{fill:var(--ink)}
.tab svg .w{fill:none;stroke:currentColor;stroke-width:2;stroke-linecap:round;stroke-linejoin:round}
</style>
</head>
<body>
<main class="screen">
  <header class="header">
    <div class="status-bar">
      <svg class="signal" width="44" height="16" viewBox="0 0 44 16"><rect x="0" y="10" width="3" height="5" fill="#fff"/><rect x="5" y="7" width="3" height="8" fill="#fff"/><rect x="10" y="4" width="3" height="11" fill="#fff"/><rect x="15" y="1" width="3" height="14" fill="#fff"/><path d="M26 7a11 11 0 0 1 16 0M29 10a6 6 0 0 1 10 0" fill="none" stroke="#fff" stroke-width="2"/><circle cx="34" cy="13" r="1.6" fill="#fff"/></svg>
      <span class="time">9:41 AM</span>
      <span class="battery"><svg width="10" height="16" viewBox="0 0 10 16"><path d="M1 4l8 8-4 3V1l4 3-8 8" fill="none" stroke="#fff" stroke-width="1.5"/></svg>100%<svg width="38" height="16" viewBox="0 0 38 16"><rect x="1" y="1" width="33" height="14" rx="3" fill="none" stroke="#fff" stroke-width="1.5"/><rect x="3" y="3" width="29" height="10" rx="1.5" fill="#fff"/><rect x="35" y="5" width="2" height="6" fill="#fff"/></svg></span>
    </div>
    <div class="brand"><span class="dot"></span>Kalvor</div>
    <div class="header-actions">
      <svg width="38" height="38" viewBox="0 0 38 38"><path d="M9 28l3-4V16a8 8 0 0 1 16 0v8l3 4z M16 31a3.5 3.5 0 0 0 7 0" fill="none" stroke="#fff" stroke-width="2" stroke-linejoin="round" transform="rotate(15 19 19)"/></svg>
      <svg width="38" height="38" viewBox="0 0 38 38"><circle cx="19" cy="19" r="5" fill="none" stroke="#fff" stroke-width="2"/><path d="M17 4h4l1 4 3 1 3-2 3 3-2 3 1 3 4 1v4l-4 1-1 3 2 3-3 3-3-2-3 1-1 4h-4l-1-4-3-1-3 2-3-3 2-3-1-3-4-1v-4l4-1 1-3-2-3 3-3 3 2 3-1z" fill="none" stroke="#fff" stroke-width="2" stroke-linejoin="round"/></svg>
    </div>
    <h1 class="employee-name">Daniel Ashcombe</h1>
  </header>
  <div class="avatar" role="img" aria-label="Employee profile photo"></div>
  <p class="employee-id">EM1104</p>

  <h2 class="section-title" style="top:248px">Attendance</h2>
  <div class="tiles attendance" style="top:300px;height:150px;padding-top:8px">
    <div class="tile"><svg viewBox="0 0 52 52"><circle class="line" cx="24" cy="15" r="9"/><path class="line" d="M8 44c0-9 7-15 16-15s13 4 15 8"/><path class="line" d="M8 44h24"/><path class="hot" d="M34 40l4 4 7-9"/></svg>Take<br>Attendance</div>
    <div class="tile"><svg viewBox="0 0 52 52"><rect class="line" x="6" y="9" width="40" height="36" rx="4"/><path class="hot" d="M16 5v8M36 5v8M24 9h4"/><g class="dotfill"><circle cx="17" cy="22" r="2"/><circle cx="26" cy="22" r="2"/><circle cx="35" cy="22" r="2"/><circle cx="17" cy="31" r="2"/><circle cx="26" cy="31" r="2"/><circle cx="35" cy="31" r="2"/></g></svg>Today</div>
    <div class="tile"><svg viewBox="0 0 52 52"><path class="line" d="M5 14h14l4 4h22v6"/><path class="line" d="M5 14v26h20"/><path class="line" d="M5 24h40l-4 14"/><circle class="hot" cx="36" cy="37" r="7"/><path class="hot" d="M36 33v4h3"/></svg>Past<br>Records</div>
    <div class="tile"><svg viewBox="0 0 52 52"><path class="line" d="M26 36c-7-8-11-13-11-19a11 11 0 0 1 22 0c0 6-4 11-11 19z"/><circle class="hot" cx="26" cy="17" r="4"/><path class="line" d="M14 32l-8 14h40l-8-14"/></svg>Station</div>
  </div>
  <div class="rule" style="top:452px"></div>

  <h2 class="section-title" style="top:483px">Sales</h2>
  <div class="tiles" style="top:541px">
    <div class="tile"><svg viewBox="0 0 52 52"><rect class="line" x="6" y="15" width="40" height="9"/><path class="line" d="M9 24v21h34V24M26 15v30"/><path class="hot" d="M26 14c-3-6-10-7-10-3s7 3 10 3c3 0 10 1 10-3s-7-3-10 3"/></svg>New<br>Redemption</div>
    <div class="tile"><svg viewBox="0 0 52 52"><path class="line" d="M4 26c6-9 14-13 22-13s16 4 22 13c-6 9-14 13-22 13S10 35 4 26z"/><circle class="hot" cx="26" cy="26" r="7"/><path class="hot" d="M26 22a4 4 0 0 0-4 4"/></svg>View<br>Redemptions</div>
    <div class="tile"><svg viewBox="0 0 52 52"><rect class="line" x="5" y="14" width="42" height="30" rx="4"/><path class="line" d="M18 14l3-5h10l3 5"/><circle class="hot" cx="26" cy="29" r="8"/><path class="hot" d="M39 20h3"/></svg>Take<br>Photo</div>
    <div class="tile"><svg viewBox="0 0 52 52"><rect class="line" x="4" y="8" width="44" height="28" rx="3"/><path class="line" d="M26 36v8M17 45h18"/><path class="hot" d="M12 29l9-9 6 5 10-11M33 14h4v4"/></svg>Sales<br>Summary</div>
  </div>
  <div class="rule" style="top:686px"></div>

  <h2 class="section-title" style="top:717px">Inventory</h2>
  <div class="tiles" style="top:775px">
    <div class="tile"><svg viewBox="0 0 52 52"><rect class="line" x="9" y="7" width="32" height="40" rx="2"/><path class="line" d="M20 5h10v5H20z"/><path class="line" d="M15 19h20M15 26h20M15 33h14"/><path class="hot" d="M33 42l3 3 7-8"/></svg>Inventory<br>Check</div>
    <div class="tile"><svg viewBox="0 0 52 52"><path class="line" d="M10 14h24v22H10M34 20h7l6 8v8h-4"/><circle class="line" cx="16" cy="38" r="4"/><circle class="line" cx="40" cy="38" r="4"/><path class="line" d="M20 36h16"/><path class="hot" d="M3 20h12M5 26h10M3 32h8"/></svg>Delivery</div>
    <div class="tile"><svg viewBox="0 0 52 52"><path class="line" d="M8 14h36l-3 32H11z"/><path class="line" d="M12 6h28l4 8"/><path class="hot" d="M20 22c0 8 12 8 12 0"/></svg>New<br>Stock Take</div>
    <div class="tile"><svg viewBox="0 0 52 52"><path class="line" d="M10 5h22l10 10v32H10z"/><path class="line" d="M32 5v10h10"/><path class="hot" d="M17 26h18M17 33h18"/><path class="line" d="M17 40h12"/></svg>Stock<br>Take List</div>
  </div>

  <nav class="tab-bar">
    <div class="tab active"><svg viewBox="0 0 40 40"><rect class="w" x="3" y="3" width="14" height="14" rx="1"/><rect class="w" x="23" y="3" width="14" height="14" rx="1"/><rect class="w" x="3" y="23" width="14" height="14" rx="1"/><rect class="w" x="23" y="23" width="14" height="14" rx="1"/></svg>Dashboard</div>
    <div class="tab"><svg viewBox="0 0 40 40"><rect class="w" x="3" y="6" width="34" height="31" rx="3"/><path class="w" d="M11 3v6M29 3v6M18 6h4"/><g fill="currentColor"><circle cx="13" cy="18" r="1.6"/><circle cx="20" cy="18" r="1.6"/><circle cx="27" cy="18" r="1.6"/><circle cx="13" cy="26" r="1.6"/><circle cx="20" cy="26" r="1.6"/><circle cx="27" cy="26" r="1.6"/></g></svg>Calendar</div>
    <div class="tab"><svg viewBox="0 0 40 40"><path class="w" d="M11 29a12 12 0 0 1 11-22M22 3l2 4-4 2M29 11a12 12 0 0 1-11 22M18 37l-2-4 4-2"/></svg>Sync</div>
    <div class="tab"><svg viewBox="0 0 40 40"><circle class="w" cx="20" cy="13" r="9"/><path class="w" d="M4 37c0-9 7-14 16-14s16 5 16 14z"/></svg>Profile</div>
  </nav>
</main>
</body>
</html>
```